Very personalised Wedding Invitation

I want a wedding invitation very unique and personalised with the menus, ceremony time table and thank you cards. I want a mix of a nice traditional style with indian style touch. I don't want a colourful invitation, it can have max. two different colours.

The bride's name is Rosalind and the groom's name is Tarun

Reason: None of the designs submitted are what I am looking for

Target Market(s)

Invitations, personalised invitations,

Industry/Entity Type

Wedding

Logo Text

Our initials T&R To use in our wedding things

Font styles to use
Decorative
Script

Requirements
Must have
Nice to have
• I would like a chic design with a bit of indian style
Should not have

```html
<!DOCTYPE html>
<html lang="en">
<head>
<meta charset="utf-8">
<title>Rosalind &amp; Tarun — Wedding Stationery</title>
<link rel="stylesheet" href="https://fonts.googleapis.com/css2?family=Cinzel:wght@400;700&family=Great+Vibes&display=swap">
<style>
  :root {
    --paper: #fdf386;
    --gold: #b8841c;
    --gold-soft: #fcd77c;
    --frame: #f4d878;
    --edge: #e9d27a;
    --canvas: #ffffff;
  }
  * { box-sizing: border-box; margin: 0; padding: 0; }
  html, body { width: 1200px; height: 682px; overflow: hidden; background: var(--canvas); }
  .sheet { position: relative; width: 1200px; height: 682px; }

  .card {
    position: absolute;
    background: var(--paper);
    border: 1px solid var(--edge);
    overflow: hidden;
    color: var(--gold);
    font-family: "Cinzel", "Times New Roman", serif;
  }
  .card svg.frames { position: absolute; inset: 0; pointer-events: none; }

  .cover { left: 22px; top: 26px; width: 411px; height: 290px; }
  .invitation { left: 456px; top: 26px; width: 410px; height: 580px; }
  .menu-card { left: 889px; top: 26px; width: 289px; height: 409px; }
  .rsvp { left: 896px; top: 456px; width: 276px; height: 192px; }

  .fold { position: absolute; left: 0; right: 0; top: 289px; border-top: 1px solid var(--edge); }

  .line {
    position: absolute; left: 0; right: 0;
    text-align: center; font-size: 8.5px; line-height: 10px; letter-spacing: 0.2px;
    white-space: nowrap;
  }
  .line.small { font-size: 7px; line-height: 9px; }
  .heading { font-weight: 700; font-size: 9px; }
  .name {
    font-family: "Great Vibes", "Brush Script MT", cursive;
    font-size: 40px; line-height: 40px; letter-spacing: 0;
  }
  .rsvp .name { font-size: 29px; line-height: 30px; }
  .dots {
    display: block; margin: 0 auto;
    border-bottom: 1px dotted var(--gold); height: 1px;
  }
  .fill { display: inline-block; width: 48px; border-bottom: 1px dotted var(--gold); margin-left: 3px; }

  .monogram {
    position: absolute; left: 0; right: 0; text-align: center;
    font-family: "Cinzel", "Times New Roman", serif; font-weight: 700;
    color: var(--gold); letter-spacing: 1px;
  }
  .cover .monogram { top: 117px; font-size: 48px; line-height: 56px; }
  .menu-card .monogram { top: 32px; font-size: 34px; line-height: 36px; }

  .menu-title { position: absolute; left: 0; right: 0; top: 88px; text-align: center; font-size: 15px; line-height: 18px; }
  .menu-rule { position: absolute; left: 88px; width: 113px; top: 108px; border-top: 1px solid var(--gold); }

  .ornament { position: absolute; }
  .ornament.tl { background: radial-gradient(ellipse at top left, var(--gold-soft) 0%, rgba(252,215,124,0.55) 40%, rgba(252,215,124,0) 72%); }
  .ornament.tr { background: radial-gradient(ellipse at top right, var(--gold-soft) 0%, rgba(252,215,124,0.55) 40%, rgba(252,215,124,0) 72%); }
  .ornament.bl { background: radial-gradient(ellipse at bottom left, var(--gold-soft) 0%, rgba(252,215,124,0.55) 40%, rgba(252,215,124,0) 72%); }
  .ornament.br { background: radial-gradient(ellipse at bottom right, var(--gold-soft) 0%, rgba(252,215,124,0.55) 40%, rgba(252,215,124,0) 72%); }
</style>
</head>
<body>
<main class="sheet">

  <section class="card cover" aria-label="Invitation cover">
    <div class="ornament tl" style="left:0;top:0;width:200px;height:170px" role="img" aria-label="Gold damask scroll ornament in top left corner"></div>
    <div class="ornament tr" style="right:0;top:0;width:200px;height:170px" role="img" aria-label="Gold damask scroll ornament in top right corner"></div>
    <div class="ornament bl" style="left:0;bottom:0;width:200px;height:170px" role="img" aria-label="Gold damask scroll ornament in bottom left corner"></div>
    <div class="ornament br" style="right:0;bottom:0;width:200px;height:170px" role="img" aria-label="Gold damask scroll ornament in bottom right corner"></div>
    <div class="monogram">T&amp;R</div>
  </section>

  <section class="card invitation" aria-label="Wedding invitation">
    <svg class="frames" width="410" height="580" viewBox="0 0 410 580" fill="none" stroke="var(--frame)" stroke-width="1.2">
      <path d="M26 12 H386 A12 12 0 0 0 398 24 V264 A12 12 0 0 0 386 276 H26 A12 12 0 0 0 14 264 V24 A12 12 0 0 0 26 12 Z"/>
      <path d="M28 17 H384 A9 9 0 0 0 393 26 V262 A9 9 0 0 0 384 271 H28 A9 9 0 0 0 19 262 V26 A9 9 0 0 0 28 17 Z"/>
      <path d="M26 304 H386 A12 12 0 0 0 398 316 V556 A12 12 0 0 0 386 568 H26 A12 12 0 0 0 14 556 V316 A12 12 0 0 0 26 304 Z"/>
      <path d="M28 309 H384 A9 9 0 0 0 393 318 V554 A9 9 0 0 0 384 563 H28 A9 9 0 0 0 19 554 V318 A9 9 0 0 0 28 309 Z"/>
    </svg>
    <div class="fold"></div>

    <p class="line" style="top:37px">As autumn leaves</p>
    <p class="line" style="top:47px">turn their brilliant hue,</p>
    <p class="line" style="top:56px">two lovers will join and say I do</p>
    <p class="line" style="top:71px">Request the honor of your presence as</p>
    <p class="line name" style="top:98px">Rosalind</p>
    <p class="line" style="top:138px">Daughter of Mr. &amp; Mrs.<span class="fill"></span></p>
    <p class="line" style="top:171px">and</p>
    <p class="line name" style="top:190px">Tarun</p>
    <p class="line" style="top:234px">Son of Mr. &amp; Mrs.<span class="fill"></span></p>

    <div class="ornament bl" style="left:0;bottom:0;width:75px;height:130px" role="img" aria-label="Gold scroll ornament in bottom left corner"></div>
    <div class="ornament br" style="right:0;bottom:0;width:75px;height:130px" role="img" aria-label="Gold scroll ornament in bottom right corner"></div>

    <p class="line" style="top:332px">will be joined together in holy matrimony</p>
    <p class="line" style="top:342px">on Saturday, the twenty ninth of September</p>
    <p class="line" style="top:352px">two thousand and seven</p>
    <p class="line heading" style="top:384px">Ceremony</p>
    <p class="line" style="top:395px">At ten o'clock in the morning</p>
    <span class="dots" style="position:absolute;left:122px;width:165px;top:413px"></span>
    <span class="dots" style="position:absolute;left:152px;width:105px;top:424px"></span>
    <span class="dots" style="position:absolute;left:182px;width:45px;top:436px"></span>
    <p class="line heading" style="top:456px">Reception</p>
    <p class="line" style="top:467px">At twelve o'clock in the afternoon</p>
    <span class="dots" style="position:absolute;left:122px;width:165px;top:486px"></span>
    <span class="dots" style="position:absolute;left:152px;width:105px;top:497px"></span>
    <span class="dots" style="position:absolute;left:182px;width:45px;top:508px"></span>
    <p class="line" style="top:527px">Your prayers, good wishes and presence at the above occasion</p>
    <p class="line" style="top:536px">will be highly appreciated</p>
  </section>

  <section class="card menu-card" aria-label="Menu card">
    <div class="monogram">T&amp;R</div>
    <p class="menu-title">Menu</p>
    <div class="menu-rule"></div>

    <p class="line" style="top:143px">Menu<span class="fill" style="width:66px"></span></p>
    <span class="dots" style="position:absolute;left:69px;width:151px;top:162px"></span>
    <span class="dots" style="position:absolute;left:96px;width:97px;top:173px"></span>

    <p class="line" style="top:208px">Menu<span class="fill" style="width:66px"></span></p>
    <span class="dots" style="position:absolute;left:69px;width:151px;top:228px"></span>
    <span class="dots" style="position:absolute;left:96px;width:97px;top:240px"></span>

    <p class="line" style="top:275px">Menu<span class="fill" style="width:66px"></span></p>
    <span class="dots" style="position:absolute;left:69px;width:151px;top:295px"></span>
    <span class="dots" style="position:absolute;left:96px;width:97px;top:306px"></span>

    <p class="line" style="top:340px">Menu<span class="fill" style="width:66px"></span></p>
    <span class="dots" style="position:absolute;left:69px;width:151px;top:360px"></span>
    <span class="dots" style="position:absolute;left:96px;width:97px;top:372px"></span>

    <div class="ornament bl" style="left:0;bottom:0;width:66px;height:70px" role="img" aria-label="Gold scroll ornament in bottom left corner"></div>
    <div class="ornament br" style="right:0;bottom:0;width:66px;height:70px" role="img" aria-label="Gold scroll ornament in bottom right corner"></div>
  </section>

  <section class="card rsvp" aria-label="Ceremony card">
    <svg class="frames" width="276" height="192" viewBox="0 0 276 192" fill="none" stroke="var(--frame)" stroke-width="1.2">
      <path d="M19 9 H257 A10 10 0 0 0 267 19 V173 A10 10 0 0 0 257 183 H19 A10 10 0 0 0 9 173 V19 A10 10 0 0 0 19 9 Z"/>
    </svg>
    <p class="line small" style="top:22px">You are invited to wedding ceremony of</p>
    <p class="line name" style="top:35px">Rosalind</p>
    <p class="line small" style="top:66px">Daughter of Mr. &amp; Mrs.<span class="fill" style="width:38px"></span></p>
    <p class="line small" style="top:80px">and</p>
    <p class="line name" style="top:86px">Tarun</p>
    <p class="line small" style="top:115px">Son of of Mr. &amp; Mrs.<span class="fill" style="width:38px"></span></p>
    <p class="line small heading" style="top:135px;font-size:7px">Ceremony</p>
    <p class="line small" style="top:145px">At ten o'clock in the morning</p>
    <span class="dots" style="position:absolute;left:58px;width:160px;top:160px"></span>
    <span class="dots" style="position:absolute;left:88px;width:100px;top:169px"></span>
  </section>

</main>
</body>
</html>
```